Webdesign für Brandt Maler
Zielgruppe
Maler- und Bodenlegerarbeiten, Farbenherstellung, Fachmarkt
ZieIgruppe sind alle, die Fraben und/oder die Dienstleistungen der Firma benötigen
Aufgabenstellung
dem Kunde gefällt die Seite http://www.maler-quirinus.example/
bitte alle Uploads beachten
eigene Bilder und Stockmaterial

```html
<!DOCTYPE html>
<html lang="de">
<head>
<meta charset="utf-8">
<title>Brandt Maler – Webdesign</title>
<link href="https://fonts.googleapis.com/css2?family=Roboto:wght@300;400;500;700&family=Work+Sans:wght@400;500;600&family=Noto+Serif:ital@1&display=swap" rel="stylesheet">
<style>
:root{
  --blue:#0b5a9a;--orange:#ee8e36;--yellow:#f0b800;--green:#74bb12;--red:#d21b1b;
  --brand-red:#cc0000;--indigo:#363399;--nav:#3a3aa0;--ink:#1b1b1b;--grey:#8a8a8a;
  --footer:#262628;--footer-bar:#333336;--stage:#ffffff;
}
*{margin:0;padding:0;box-sizing:border-box}
html,body{width:857px;height:1200px;overflow:hidden;background:var(--stage)}
.page{position:absolute;left:277px;top:10px;width:564px;height:2205px;transform:scale(.535);transform-origin:0 0;background:#fff;font-family:"Work Sans",sans-serif;color:var(--ink);box-shadow:0 6px 18px rgba(0,0,0,.25)}
.abs{position:absolute}
.header{left:0;top:0;width:564px;height:42px;background:#fff}
.logo{left:0;width:564px;top:4px;text-align:center;font:700 10px "Roboto",sans-serif;color:var(--nav)}
.nav{left:0;width:564px;top:25px;display:flex;justify-content:center;gap:11px;font:400 5.5px "Roboto",sans-serif;color:var(--nav)}
.hero{left:0;top:42px;width:564px;height:259px;background:linear-gradient(100deg,#3d4148 0%,#5a5e66 35%,#c9c7c0 55%,#e3e1da 100%)}
.hero h1{position:absolute;left:75px;top:100px;font:600 16px "Work Sans",sans-serif;color:#fff;letter-spacing:.3px;text-shadow:0 1px 3px rgba(0,0,0,.6)}
.hero p{position:absolute;left:75px;top:127px;font:600 11px "Work Sans",sans-serif;color:#fff;text-shadow:0 1px 3px rgba(0,0,0,.6)}
.btn{position:absolute;background:var(--brand-red);color:#fff;font:400 6.5px "Roboto",sans-serif;display:flex;align-items:center;justify-content:center}
.hero .btn{left:243px;top:149px;width:77px;height:22px}
.h2{font:500 13px "Roboto",sans-serif}
.services{left:71px;top:345px;width:422px;height:379px;display:grid;grid-template-columns:141px 141px 140px;grid-template-rows:205px 174px}
.tile{padding:16px 18px 0;color:#fff}
.tile svg{display:block;margin:0 0 8px 36px}
.tile h3{font:500 9px "Work Sans",sans-serif;line-height:9px;margin-bottom:6px}
.tile p{font:400 6px/10px "Work Sans",sans-serif}
.t-blue{background:var(--blue)}.t-orange{background:var(--orange)}.t-yellow{background:var(--yellow)}
.t-green{background:var(--green)}.t-red{background:var(--red);grid-column:span 2}
.news h2{font:500 11px "Work Sans",sans-serif;margin-bottom:6px}
.serif{font:italic 7px/11.3px "Noto Serif",serif;color:#555}
.splash{left:295px;top:785px;width:175px;height:115px;background:radial-gradient(ellipse at 55% 60%,#e63b2e 0%,#f5b400 25%,#2fa6e0 45%,#7cc242 60%,rgba(255,255,255,0) 75%)}
.about-band{left:0;top:958px;width:564px;height:120px;background:var(--indigo);color:#fff;text-align:center}
.about-band h2{margin-top:40px;font:400 16px "Work Sans",sans-serif}
.about-band p{margin-top:6px;font:600 10px "Work Sans",sans-serif;letter-spacing:.5px}
.firm h2{font:500 11px "Work Sans",sans-serif;margin-bottom:6px}
.small-grey{font:300 5px/8.4px "Roboto",sans-serif;color:var(--grey)}
.photo{position:absolute}
.refs-title{left:0;width:574px;top:1400px;text-align:center;font:500 11px "Work Sans",sans-serif}
.rule{left:273px;top:1422px;width:27px;height:1px;background:#333}
.refs-text{left:150px;width:274px;top:1432px;text-align:left;font:300 7.5px/14.5px "Roboto",sans-serif;color:var(--grey)}
.dots{left:273px;top:1598px;display:flex;gap:5px}
.dots i{width:3px;height:3px;border-radius:50%;background:#ccc}.dots i.on{background:#444}
.contact{left:0;top:1648px;width:564px;height:307px;background:var(--brand-red)}
.contact h2{position:absolute;left:78px;top:14px;font:500 13px "Roboto",sans-serif;color:#fff}
.form{position:absolute;left:74px;top:48px;width:415px;height:244px;background:#fff}
.field{position:absolute;left:6px;font:700 4.5px "Roboto",sans-serif;color:#333}
.line{position:absolute;left:6px;height:1px;background:#ddd}
.form .btn{left:6px;top:205px;width:41px;height:17px;font-size:4.5px}
.footer{left:0;top:1955px;width:564px;height:205px;background:var(--footer);color:#ddd}
.footer h4{font:400 7px "Work Sans",sans-serif;color:#fff;margin-bottom:16px}
.fcol{position:absolute;top:36px;font:400 5px/13.6px "Roboto",sans-serif}
.fcol .mail{color:var(--brand-red)}
.map{position:absolute;left:360px;top:113px;width:126px;height:54px;background:linear-gradient(120deg,#dfe9f2 0%,#eef1ee 40%,#d7ecd3 100%)}
.bar{left:0;top:2160px;width:564px;height:45px;background:var(--footer-bar)}
.bar nav{position:absolute;left:76px;top:17px;display:flex;gap:12px;font:500 4px "Roboto",sans-serif;color:#fff}
.bar .copy{position:absolute;right:72px;top:16px;font:400 4px/8px "Roboto",sans-serif;color:#ddd}
</style>
</head>
<body>
<div class="page">
  <header class="header abs">
    <div class="logo abs">Brandt Maler</div>
    <nav class="nav abs"><span>HOME</span><span>LEISTUNGEN</span><span>AKTUELLE MELDUNGEN</span><span>ÜBER UNS</span><span>REFERENZEN</span><span>KONTAKT</span></nav>
  </header>

  <section class="hero abs" role="img" aria-label="Farbroller mit Firmenaufdruck auf frisch gestrichener Wand">
    <h1>IHR PROFI MIT LANGJÄHRIGER ERFAHRUNG</h1>
    <p>Maler - Bodenlegerarbeiten - Farbenherstellung - Fachmarkt</p>
    <span class="btn">Anfrage stellen</span>
  </section>

  <h2 class="h2 abs" style="left:71px;top:322px">Unsere Leistungen</h2>
  <section class="services abs">
    <div class="tile t-blue">
      <svg width="34" height="32" viewBox="0 0 34 32" fill="none" stroke="#fff" stroke-width="1.3"><rect x="3" y="4" width="22" height="24"/><path d="M8 22l18-18 4 4-18 18H8z"/></svg>
      <h3>Planung &amp; Beratung</h3>
      <p>Durch eine ausführliche Planung und kompetente Fachberatung, welche wir in unserem Fachmarkt oder vor Ort durchführen, haben unsere Kunden stets eine exakte Übersicht über die anfallenden Kosten und können sich von der Transparenz eines jeweiligen Angebotes überzeugen.</p>
    </div>
    <div class="tile t-orange">
      <svg width="34" height="32" viewBox="0 0 34 32" fill="none" stroke="#fff" stroke-width="1.3"><rect x="3" y="2" width="28" height="28"/><path d="M3 16L17 2M3 30L31 2M17 30L31 16M3 2l28 28M3 16l14 14M17 2l14 14"/></svg>
      <h3>Fußbodenarbeiten</h3>
      <p>Wir überlassen nichts dem Zufall. Hochwertige Materialien und Rohstoffe sowie der Einsatz von Qualitätswerkzeugen sorgen für eine perfekte Qualität bei der Auftragsausführung unseres motivierten Fachpersonals.</p>
    </div>
    <div class="tile t-yellow">
      <svg width="34" height="32" viewBox="0 0 34 32" fill="none" stroke="#fff" stroke-width="1.3"><rect x="4" y="3" width="22" height="8" rx="2"/><path d="M26 7h4v8H16v5M14 20h4v10h-4z"/></svg>
      <h3>Fassaden &amp;<br>Wandgestaltung</h3>
      <p>Benötigt Ihr Haus einen neuen Anstrich oder eine attraktive Fassade? Gern sind wir für diese anspruchsvolle Aufgabe Ihr Ansprechpartner. Wir geben Ihrer Immobilie wieder ein neues Aussehen. Stilvoll und elegant.</p>
    </div>
    <div class="tile t-green">
      <svg width="34" height="32" viewBox="0 0 34 32" fill="none" stroke="#fff" stroke-width="1.3"><path d="M9 3h16v9l-5 4v13h-6V16l-5-4z"/></svg>
      <h3>Tapezier &amp;<br>Malerarbeiten</h3>
      <p>Ein neues Ambiente im Wohnbereich, gestaltet mit hochwertiger Tapete oder Raumfarbe lässt Sie wieder entspannter relaxen und macht Ihre Wohnung zu einem echten Paradies.</p>
    </div>
    <div class="tile t-red">
      <svg width="34" height="32" viewBox="0 0 34 32" fill="none" stroke="#fff" stroke-width="1.3"><circle cx="13" cy="9" r="5"/><path d="M4 30v-8a9 9 0 0118 0v8"/><circle cx="25" cy="13" r="6"/></svg>
      <h3>Dienstleistungen &amp; Service</h3>
      <p style="width:300px">Ein neues Ambiente im Wohnbereich, gestaltet mit hochwertiger Tapete oder Raumfarbe lässt Sie wieder entspannter relaxen und macht Ihre Wohnung zu einem echten Paradies</p>
    </div>
  </section>

  <section class="news abs" style="left:76px;top:761px;width:188px">
    <h2>Aktuelle Meldungen</h2>
    <p class="serif">Lorem ipsum dolor sit amet, consetetur sadipscing elitr, sed diam nonumy eirmod tempor invidunt ut labore et dolore magna aliquyam erat, sed diam voluptua. At vero eos et accusam et justo duo dolores et ea rebum. Stet clita kasd gubergren, no sea takimata sanctus est Lorem ipsum dolor sit amet. Lorem ipsum dolor sit amet, consetetur sadipscing elitr, sed diam nonumy eirmod tempor invidunt ut labore et dolore magna aliquyam erat, sed diam voluptua. At vero eos et accusam et justo duo dolores et ea rebum. Stet clita kasd gubergren, no sea takimata sanctus est Lorem ipsum dolor sit amet.</p>
  </section>
  <div class="splash abs" role="img" aria-label="Bunte Farbspritzer in Rot, Gelb, Blau und Grün"></div>

  <section class="about-band abs">
    <h2>Über uns</h2>
    <p>- Mit 100jähriger Erfahrung -</p>
  </section>

  <section class="firm abs" style="left:74px;top:1126px;width:118px">
    <h2>Unsere Firma</h2>
    <p class="serif" style="font-size:6.5px;line-height:11px;margin-bottom:6px">Die Firma Brandt Maler wurde 1919 gegründet und ist ein seit mehreren Generationen geführtes Familienunternehmen</p>
    <p class="small-grey">Lorem ipsum dolor sit amet, consetetur sadipscing elitr, sed diam nonumy eirmod tempor invidunt ut labore et dolore magna aliquyam erat, sed diam voluptua. At vero eos et accusam et justo duo dolores et ea rebum. Stet clita kasd gubergren, no sea takimata sanctus est Lorem ipsum dolor sit amet. Lorem ipsum dolor sit amet, consetetur sadipscing elitr, sed diam nonumy eirmod tempor invidunt ut labore et dolore magna aliquyam erat, sed diam voluptua. At vero eos et accusam et justo duo dolores et ea rebum. Stet clita kasd gubergren, no sea takimata sanctus est Lorem ipsum dolor sit amet.</p>
  </section>
  <div class="photo" style="left:202px;top:1133px;width:161px;height:187px;background:linear-gradient(180deg,#8fa2b8 0%,#ece6da 30%,#d8cfc0 70%,#6b5d50 100%)" role="img" aria-label="Firmengebäude mit Ladengeschäft"></div>
  <div class="photo" style="left:365px;top:1133px;width:128px;height:92px;background:linear-gradient(160deg,#c9c3b8,#6e655c)" role="img" aria-label="Verkaufsraum im Fachmarkt"></div>
  <div class="photo" style="left:365px;top:1227px;width:128px;height:93px;background:linear-gradient(160deg,#e4e0da,#8a8076)" role="img" aria-label="Ausstellungsfläche mit Bodenbelägen"></div>

  <h2 class="refs-title abs">Unsere Referenzen</h2>
  <div class="rule abs"></div>
  <p class="refs-text abs">Zahlreiche Unternehmen, Betriebe oder Privatpersonen zählen seit Jahren zu unseren Stammkunden. Eine Vielzahl von Projekten konnten dabei verwirklicht und umgesetzt werden.</p>
  <div class="photo" style="left:71px;top:1501px;width:139px;height:94px;background:linear-gradient(120deg,#b9bcbf,#e7d64a 60%,#8c8f91)" role="img" aria-label="Treppenhaus mit gelber Wand"></div>
  <div class="photo" style="left:217px;top:1501px;width:140px;height:94px;background:linear-gradient(180deg,#2d6fc4 0%,#6aa0dd 40%,#a8714a 65%,#5e4a36 100%)" role="img" aria-label="Historisches Rathaus mit Turm"></div>
  <div class="photo" style="left:365px;top:1501px;width:139px;height:94px;background:linear-gradient(180deg,#f2f2f2,#c9a77a 70%,#9a9a9a)" role="img" aria-label="Heller Saal mit Holztüren"></div>
  <div class="dots abs"><i></i><i class="on"></i><i></i><i></i></div>

  <section class="contact abs">
    <h2>Schreiben Sie uns</h2>
    <form class="form">
      <span class="field" style="top:8px">Ihr Name</span><span class="line" style="top:27px;width:122px"></span>
      <span class="field" style="top:39px">Ihre E-Mail</span><span class="line" style="top:58px;width:122px"></span>
      <span class="field" style="top:69px">Betreff</span><span class="line" style="top:88px;width:122px"></span>
      <span class="field" style="top:99px">Ihre Nachricht</span><span class="line" style="top:191px;width:129px"></span>
      <span class="btn">SENDEN</span>
    </form>
  </section>

  <footer class="footer abs">
    <div class="fcol" style="left:74px">
      <h4>Kontakt</h4>
      <b style="font-weight:500">Brandt Maler GmbH</b><br>Lindenweg 8<br>04711 Grünfeld<br>Sachsen/Deutschland<br>Tel.: 03412 55184<br>Fax: 03412 55185<br>Mobil: 0170 4418290<br>E-Mail: <span class="mail">info@brandt-maler.example</span>
    </div>
    <div class="fcol" style="left:215px;line-height:9.5px">
      <h4>Öffnungszeiten Musterstudio</h4>
      Montag – Freitag :<br>09:00 Uhr – 13:00 Uhr<br>15:00 Uhr – 18:00 Uhr<br><br>Samstag : Vormittags nach Vereinbarung
    </div>
    <div class="fcol" style="left:356px">
      <h4>Social Media</h4>
      <div style="display:flex;gap:6px;margin-top:-8px">
        <svg width="7" height="7"><rect width="7" height="7" fill="#fff"/></svg>
        <svg width="7" height="7"><rect width="7" height="7" fill="#fff"/></svg>
        <svg width="7" height="7"><rect width="7" height="7" fill="#fff"/></svg>
        <svg width="7" height="7"><rect width="7" height="7" fill="#fff"/></svg>
      </div>
      <h4 style="margin-top:20px">Anfahrt</h4>
    </div>
    <div class="map" role="img" aria-label="Lageplan mit Standortmarkierung"></div>
  </footer>

  <div class="bar abs">
    <nav><span>HOME</span><span>LEISTUNGEN</span><span>AKTUELLE MELDUNGEN</span><span>ÜBER UNS</span><span>REFERENZEN</span><span>KONTAKT</span></nav>
    <div class="copy">Impressum I Datenschutz I Kontakt<br>copyright Brandt Maler GmbH 2021</div>
  </div>
</div>
</body>
</html>
```